Ferncrest Dental, LLC business card project

Business card to be designed with current logo.
Dental office- please keep design of card that looks clean and professional.
Please include the following info:
Ferncrest Dental, LLC
Dr. Lorna Pettigrew
2871 Marlowe Street
Bethlehem, PA 18093
610-555-0193
ferncrestdental.office@examplemail.test
Hello everyone-
Reason: Just got back from overseas- will look at all designs and provide feedback. Thank you!
Reason: Polling my friends for the final selection-
thank you to all those that participated- so many talented designers!

```html
<!DOCTYPE html>
<html lang="en">
<head>
<meta charset="utf-8">
<title>Ferncrest Dental, LLC – Business Card</title>
<link rel="stylesheet" href="https://fonts.googleapis.com/css2?family=Questrial&display=swap">
<style>
  :root {
    --page-bg: #e9eaea;
    --card-bg: #ffffff;
    --brand-green: #6fa52a;
    --text-green: #4e8a22;
    --card-shadow: rgba(0, 0, 0, 0.12);
  }
  * { margin: 0; padding: 0; box-sizing: border-box; }
  html, body {
    width: 1198px;
    height: 1200px;
    overflow: hidden;
    background: var(--page-bg);
    font-family: "Questrial", "Century Gothic", sans-serif;
  }
  .sheet {
    width: 1198px;
    height: 1200px;
    display: flex;
    flex-direction: column;
    align-items: center;
    justify-content: center;
    gap: 44px;
  }
  .card {
    position: relative;
    width: 900px;
    height: 514px;
    background: var(--card-bg);
    box-shadow: 0 6px 24px var(--card-shadow);
    color: var(--text-green);
  }
  .brand {
    position: absolute;
    display: flex;
    align-items: center;
    gap: 14px;
    color: var(--brand-green);
    font-size: 38px;
    letter-spacing: 0.2px;
  }
  .brand-dot {
    width: 22px;
    height: 22px;
    border-radius: 50%;
    background: var(--brand-green);
  }
  .card-front .brand { top: 52px; right: 60px; }
  .holder-name {
    position: absolute;
    left: 60px;
    top: 196px;
    padding-left: 16px;
    border-left: 2px solid var(--text-green);
    font-size: 34px;
    line-height: 40px;
    letter-spacing: 1px;
  }
  .contact-block {
    position: absolute;
    left: 60px;
    bottom: 58px;
    padding-left: 18px;
    border-left: 2px solid var(--text-green);
    font-size: 23px;
    line-height: 30px;
    letter-spacing: 0.5px;
  }
  .contact-block .address { margin-bottom: 16px; }
  .contact-block .phone { margin-bottom: 6px; }
  .social-list {
    position: absolute;
    right: 60px;
    top: 222px;
    list-style: none;
    font-size: 22px;
    line-height: 34px;
  }
  .social-list li { display: flex; align-items: center; gap: 12px; }
  .social-square {
    width: 22px;
    height: 22px;
    border-radius: 3px;
    background: var(--text-green);
  }
  .card-back .brand {
    top: 200px;
    left: 60px;
    font-size: 46px;
  }
  .card-back .brand-dot { width: 26px; height: 26px; }
  .website {
    position: absolute;
    right: 60px;
    bottom: 56px;
    font-size: 18px;
    letter-spacing: 0.4px;
  }
</style>
</head>
<body>
  <main class="sheet">
    <section class="card card-front" aria-label="Business card front">
      <div class="brand"><span class="brand-dot"></span><span class="brand-name">Ferncrest Dental, LLC</span></div>
      <h1 class="holder-name">Dr. Lorna Pettigrew</h1>
      <address class="contact-block">
        <p class="address">2871 Marlowe Street<br>Bethlehem, PA 18093</p>
        <p class="phone">610-555-0193</p>
        <p class="email">ferncrestdental.office@examplemail.test</p>
      </address>
      <ul class="social-list">
        <li><span class="social-square"></span>FerncrestDental.555</li>
        <li><span class="social-square"></span>@FerncrestDental</li>
      </ul>
    </section>
    <section class="card card-back" aria-label="Business card back">
      <div class="brand"><span class="brand-dot"></span><span class="brand-name">Ferncrest Dental, LLC</span></div>
      <p class="website">www.ferncrestdental.test</p>
    </section>
  </main>
</body>
</html>
```